An envelope for Housekeepers / The Marigold Sleeve

Globally, 212 million people are employed in the hospitality industry. While many get commemorated for their work, there is one job that is often looked over.
Housekeepers hardly ever get told how great of a job they are doing.
Our company QuillNestly is seeking to empower housekeepers by allowing our guests to tip them through a cool envelope.
The plan :
- Create an envelope that has a message on it, which will incentivize our clientele to tip their housekeepers at check-out, and give housekeepers the credit they deserve for their hard work.
Example :
- "Humans do well by doing good" / "a thank you for your housekeeper"
What to do :
- Create an envelope based on the attached file. The white page titled "The Marigold Sleeve" will be the front of the envelope (feel free to improve it but we really like the concept of it). The four blue pages will be the back pages of the envelope. Feel free to scour the web for quotes & embodying the same message of generosity.
We are really looking forward to seeing what kind of creative envelope you can conjure.
PS : remember that the goal with this envelope is to empower housekeepers & incentivize guests to tip them.
Target Market(s)
Travelers & housekeepers
Industry/Entity Type
Hospitality
Other font styles liked:
- Trebuchet, Times New Roman
Requirements
Must have
- Our project must have :
- - A white first page titled "The Marigold Sleev" is a must
- - You can improve it, but do not change the concept of it
- - Font : simple & easy to read
- - Color of back page : Teal
Nice to have
- Always keep in mind that this envelope is made to empower housekeepers.
Should not have
- Just keep it simple. Don't complicate things.

```html
<!DOCTYPE html>
<html lang="en">
<head>
<meta charset="utf-8">
<title>The Marigold Sleeve – QuillNestly</title>
<link rel="stylesheet" href="https://fonts.googleapis.com/css2?family=Jost:wght@400;700&display=swap">
<style>
  :root{
    --backdrop:#2b2b2c;
    --paper:#ffffff;
    --aqua:#a6e0df;
    --sky:#7fc8e6;
    --slate:#56777d;
    --ink:#4a4a4a;
    --fold:rgba(40,50,55,.55);
  }
  *{box-sizing:border-box;margin:0;padding:0}
  html,body{width:1200px;height:900px;overflow:hidden;background:var(--backdrop)}
  body{font-family:"Jost",Arial,sans-serif}
  .stage{position:relative;width:1488px;height:1116px;transform:scale(.80645);transform-origin:0 0}

  .envelope{position:absolute;text-align:center;text-transform:uppercase}
  .envelope__flap{position:absolute;left:0;display:block}
  .envelope__body{position:absolute;left:0;top:0;width:100%;height:100%}

  /* fronts */
  .front .envelope__body{background:var(--paper)}
  .front .title{position:absolute;left:0;right:0;font-weight:400;letter-spacing:.02em}
  .front .by{position:absolute;left:0;right:0;color:var(--ink);letter-spacing:.08em}
  .brand{position:absolute;left:0;right:0;display:flex;justify-content:center;align-items:center;color:var(--ink);text-transform:none}
  .brand__dot{border:1.5px solid var(--ink);border-radius:50%;display:inline-block}

  /* backs */
  .back .quote{position:absolute;left:0;right:0;font-weight:700;color:var(--paper)}
  .back .author{position:absolute;left:0;right:0;color:var(--paper);font-weight:400}
  .back .note{position:absolute;left:0;right:0;color:var(--paper);letter-spacing:.2em}
  .back .fold-line{position:absolute;left:0;top:0}

  /* small size */
  .sm{width:169px;height:352px}
  .sm.front .envelope__flap{top:-53px}
  .sm .title{top:130px;font-size:24px;line-height:31px}
  .sm .by{top:290px;font-size:8px}
  .sm .brand{top:306px;gap:6px;font-size:11px}
  .sm .brand__dot{width:20px;height:20px}
  .sm .quote{top:121px;font-size:17px;line-height:23px}
  .sm .author{top:214px;font-size:11.5px}
  .sm .note{top:304px;font-size:7.5px;line-height:14px}

  /* large size */
  .lg{width:234px;height:418px}
  .lg.front .envelope__flap{top:-72px}
  .lg .title{top:147px;font-size:33px;line-height:42px}
  .lg .by{top:335px;font-size:10px}
  .lg .brand{top:361px;gap:8px;font-size:15px}
  .lg .brand__dot{width:29px;height:29px}
  .lg .quote{top:133px;font-size:25px;line-height:32px}
  .lg .author{top:263px;font-size:16.5px}
  .lg .note{top:361px;font-size:10.5px;line-height:19px}

  /* colourways */
  .aqua .title{color:var(--aqua)} .aqua .envelope__flap path{fill:var(--aqua)}
  .aqua.back .envelope__body{background:var(--aqua)}
  .sky .title{color:var(--sky)} .sky .envelope__flap path{fill:var(--sky)}
  .sky.back .envelope__body{background:var(--sky)}
  .slate .title{color:var(--slate)} .slate .envelope__flap path{fill:var(--slate)}
  .slate.back .envelope__body{background:var(--slate)}
</style>
</head>
<body>
<main class="stage">

  <!-- row one -->
  <article class="envelope front sm aqua" style="left:72px;top:198px">
    <svg class="envelope__flap" width="169" height="53" viewBox="0 0 169 53"><path d="M0 53 L7 12 Q84 -6 162 12 L169 53 Z"/></svg>
    <div class="envelope__body"></div>
    <h2 class="title">The<br>Marigold<br>Sleeve</h2>
    <p class="by">By</p>
    <p class="brand"><span class="brand__dot"></span>QuillNestly</p>
  </article>

  <article class="envelope back sm aqua" style="left:255px;top:198px">
    <div class="envelope__body"></div>
    <svg class="fold-line" width="169" height="60" viewBox="0 0 169 60"><path d="M3 2 L8 30 Q84 62 161 30 L166 2" fill="none" stroke="var(--fold)" stroke-width="1.2"/></svg>
    <p class="quote">“Generosity<br>isn’t an act.<br>It’s a way<br>of life.”</p>
    <p class="author">Dara Whitfield</p>
    <p class="note">A thank you for<br>your housekeeper</p>
  </article>

  <article class="envelope front lg aqua" style="left:438px;top:132px">
    <svg class="envelope__flap" width="234" height="72" viewBox="0 0 234 72"><path d="M0 72 L9 16 Q117 -8 225 16 L234 72 Z"/></svg>
    <div class="envelope__body"></div>
    <h2 class="title">The<br>Marigold<br>Sleeve</h2>
    <p class="by">By</p>
    <p class="brand"><span class="brand__dot"></span>QuillNestly</p>
  </article>

  <article class="envelope back lg aqua" style="left:686px;top:132px">
    <div class="envelope__body"></div>
    <svg class="fold-line" width="234" height="80" viewBox="0 0 234 80"><path d="M4 2 L11 46 Q117 88 223 46 L230 2" fill="none" stroke="var(--fold)" stroke-width="1.3"/></svg>
    <p class="quote">“Generosity<br>isn’t an act.<br>It’s a way<br>of life.”</p>
    <p class="author">Dara Whitfield</p>
    <p class="note">A thank you for<br>your housekeeper</p>
  </article>

  <article class="envelope front lg sky" style="left:934px;top:132px">
    <svg class="envelope__flap" width="234" height="72" viewBox="0 0 234 72"><path d="M0 72 L9 16 Q117 -8 225 16 L234 72 Z"/></svg>
    <div class="envelope__body"></div>
    <h2 class="title">The<br>Marigold<br>Sleeve</h2>
    <p class="by">By</p>
    <p class="brand"><span class="brand__dot"></span>QuillNestly</p>
  </article>

  <article class="envelope back lg sky" style="left:1183px;top:132px">
    <div class="envelope__body"></div>
    <svg class="fold-line" width="234" height="80" viewBox="0 0 234 80"><path d="M4 2 L11 46 Q117 88 223 46 L230 2" fill="none" stroke="var(--fold)" stroke-width="1.3"/></svg>
    <p class="quote">“Generosity<br>isn’t an act.<br>It’s a way<br>of life.”</p>
    <p class="author">Dara Whitfield</p>
    <p class="note">A thank you for<br>your housekeeper</p>
  </article>

  <!-- row two -->
  <article class="envelope front sm slate" style="left:72px;top:702px">
    <svg class="envelope__flap" width="169" height="53" viewBox="0 0 169 53"><path d="M0 53 L7 12 Q84 -6 162 12 L169 53 Z"/></svg>
    <div class="envelope__body"></div>
    <h2 class="title">The<br>Marigold<br>Sleeve</h2>
    <p class="by">By</p>
    <p class="brand"><span class="brand__dot"></span>QuillNestly</p>
  </article>

  <article class="envelope back sm slate" style="left:255px;top:702px">
    <div class="envelope__body"></div>
    <svg class="fold-line" width="169" height="60" viewBox="0 0 169 60"><path d="M3 2 L8 30 Q84 62 161 30 L166 2" fill="none" stroke="var(--fold)" stroke-width="1.2"/></svg>
    <p class="quote">“Generosity<br>isn’t an act.<br>It’s a way<br>of life.”</p>
    <p class="author">Dara Whitfield</p>
    <p class="note">A thank you for<br>your housekeeper</p>
  </article>

  <article class="envelope front lg slate" style="left:438px;top:636px">
    <svg class="envelope__flap" width="234" height="72" viewBox="0 0 234 72"><path d="M0 72 L9 16 Q117 -8 225 16 L234 72 Z"/></svg>
    <div class="envelope__body"></div>
    <h2 class="title">The<br>Marigold<br>Sleeve</h2>
    <p class="by">By</p>
    <p class="brand"><span class="brand__dot"></span>QuillNestly</p>
  </article>

  <article class="envelope back lg slate" style="left:686px;top:636px">
    <div class="envelope__body"></div>
    <svg class="fold-line" width="234" height="80" viewBox="0 0 234 80"><path d="M4 2 L11 46 Q117 88 223 46 L230 2" fill="none" stroke="var(--fold)" stroke-width="1.3"/></svg>
    <p class="quote">“Generosity<br>isn’t an act.<br>It’s a way<br>of life.”</p>
    <p class="author">Dara Whitfield</p>
    <p class="note">A thank you for<br>your housekeeper</p>
  </article>

  <article class="envelope front sm sky" style="left:934px;top:702px">
    <svg class="envelope__flap" width="169" height="53" viewBox="0 0 169 53"><path d="M0 53 L7 12 Q84 -6 162 12 L169 53 Z"/></svg>
    <div class="envelope__body"></div>
    <h2 class="title">The<br>Marigold<br>Sleeve</h2>
    <p class="by">By</p>
    <p class="brand"><span class="brand__dot"></span>QuillNestly</p>
  </article>

  <article class="envelope back sm sky" style="left:1117px;top:702px">
    <div class="envelope__body"></div>
    <svg class="fold-line" width="169" height="60" viewBox="0 0 169 60"><path d="M3 2 L8 30 Q84 62 161 30 L166 2" fill="none" stroke="var(--fold)" stroke-width="1.2"/></svg>
    <p class="quote">“Generosity<br>isn’t an act.<br>It’s a way<br>of life.”</p>
    <p class="author">Dara Whitfield</p>
    <p class="note">A thank you for<br>your housekeeper</p>
  </article>

</main>
</body>
</html>
```